KOVA WIRING PTE LTD
KOVA WIRING NAME CARD
Project: KOVA WIRING PTE LTD
KOVA WIRING PTE LTD - Engineering
Creative Brief
Professional
Deren Whitcombe
Manager
57 Tannery Lane #03-22 Silverbrook Industrial Complex Singapore 347912
derenkovawiring@mailbox-example.net
Reg No. 198733502K
https://www.filevault-example.net/share/7qe2kx9/ZTRmPwq4HnLc?dl=0 Pleas find folder for the logo design A.I. file. Thanks Client love the 3 colour in the logo design for FengShui purposes.
harlowbek harlowbek
Hi my client like your design #218, Can you give the stationary set for #218. We try to finalize by tomorrow. Thanks

```html
<!DOCTYPE html>
<html lang="en">
<head>
<meta charset="utf-8">
<title>KOVA WIRING – Name Card</title>
<link rel="stylesheet" href="https://fonts.googleapis.com/css2?family=Questrial&display=swap">
<style>
  :root {
    --backdrop: #e4e4e2;
    --card-white: #ffffff;
    --card-black: #0b0b0b;
    --brand-green: #1f9a48;
    --brand-navy: #1d2a5c;
    --ink-light: #f2f2f2;
    --ink-dark: #151515;
  }
  * { margin: 0; padding: 0; box-sizing: border-box; }
  html, body {
    width: 1200px; height: 901px; overflow: hidden;
    background: var(--backdrop);
    font-family: "Questrial", "Century Gothic", sans-serif;
  }
  .name-card {
    position: absolute; left: 150px; top: 180px;
    width: 900px; height: 540px;
    border-radius: 36px; overflow: hidden;
    background: var(--card-white);
    box-shadow: 0 12px 30px rgba(0,0,0,0.18);
  }
  .card-shapes { position: absolute; inset: 0; }
  .brand {
    position: absolute; left: 56px; top: 158px;
    display: flex; align-items: center; gap: 14px;
  }
  .brand-square {
    width: 62px; height: 62px; background: var(--brand-green);
  }
  .brand-name {
    font-size: 34px; letter-spacing: 2px; color: var(--brand-navy);
    line-height: 1; white-space: nowrap;
  }
  .details {
    position: absolute; right: 44px; top: 0; bottom: 0;
    text-align: right; color: var(--ink-light);
  }
  .person-name { position: absolute; right: 0; top: 92px; font-size: 24px; white-space: nowrap; }
  .person-role { position: absolute; right: 0; top: 124px; font-size: 15px; white-space: nowrap; }
  .address {
    position: absolute; right: 0; top: 196px;
    font-size: 18px; line-height: 26px; white-space: nowrap;
  }
  .contact-list {
    position: absolute; right: 0; top: 322px; list-style: none;
    font-size: 15px; white-space: nowrap;
  }
  .contact-list li {
    display: flex; justify-content: flex-end; align-items: center;
    gap: 10px; height: 30px;
  }
  .contact-list li.spaced { margin-top: 26px; }
  .contact-icon { width: 16px; height: 16px; fill: none; stroke: var(--ink-light); stroke-width: 1.6; }
</style>
</head>
<body>
  <div class="name-card">
    <svg class="card-shapes" width="900" height="540" viewBox="0 0 900 540" aria-hidden="true">
      <path d="M575 0 C470 90 430 180 470 280 C505 370 450 470 360 540 L900 540 L900 0 Z" fill="var(--card-black)"/>
      <path d="M555 0 C450 90 410 180 450 280 C482 360 445 445 375 520" fill="none" stroke="var(--brand-green)" stroke-width="7"/>
    </svg>

    <div class="brand">
      <span class="brand-square"></span>
      <span class="brand-name">KOVA WIRING</span>
    </div>

    <div class="details">
      <p class="person-name">Deren Whitcombe</p>
      <p class="person-role">Manager</p>
      <p class="address">57 Tannery Lane<br>#03-22 Silverbrook Industrial Complex<br>Singapore 347912</p>
      <ul class="contact-list">
        <li>(65) 61002481
          <svg class="contact-icon" viewBox="0 0 16 16"><path d="M3 2 L6 2 L7 5 L5 6.5 C6 9 7 10 9.5 11 L11 9 L14 10 L14 13 C14 14 13 14.5 12 14.5 C6.5 14 2 9.5 1.5 4 C1.5 3 2 2 3 2 Z"/></svg>
        </li>
        <li>(65) 90417735
          <svg class="contact-icon" viewBox="0 0 16 16"><rect x="4.5" y="1.5" width="7" height="13" rx="1.2"/><line x1="7" y1="12.5" x2="9" y2="12.5"/></svg>
        </li>
        <li class="spaced">derenkovawiring@mailbox-example.net
          <svg class="contact-icon" viewBox="0 0 16 16"><rect x="1.5" y="3.5" width="13" height="9"/><path d="M1.5 3.5 L8 9 L14.5 3.5"/></svg>
        </li>
        <li>(65) 61002481
          <svg class="contact-icon" viewBox="0 0 16 16"><rect x="4" y="1.5" width="8" height="4"/><rect x="1.5" y="5.5" width="13" height="6"/><rect x="4" y="9.5" width="8" height="5"/></svg>
        </li>
        <li>www.kovawiring-example.net
          <svg class="contact-icon" viewBox="0 0 16 16"><circle cx="8" cy="8" r="6.5"/><ellipse cx="8" cy="8" rx="3" ry="6.5"/><line x1="1.5" y1="8" x2="14.5" y2="8"/></svg>
        </li>
      </ul>
    </div>
  </div>
</body>
</html>
```